Engineering Land Development Company Needs Flyer Brochure for Prospective Professional Clients

Our company provides land development site design for commercial projects. We have many repeat clients that are familiar with our work. We do not advertise our services other than a website. Most of our referrals are from existing clients. When a new client contacts us and asks for a proposal for a project we would like to have a brochure that shows our strengths, experience, and professionalism. We are selling professional services similar to a lawyer or accountant. We want new clients to feel comfortable hiring a new firm. The brochure would be one page single-side included when we submit proposals for new projects. Check out our website at tovamrk.net for more info. We would like a brochure that mixes grading/excavation construction work on a job site with business professional. We will need to update the brochure so we want it in .doc .psd or some other edit format. The brochure we are using is attached. It is very two-dimensional. We need some depth.

Target Market(s)

Land developers, architects, real estate, professionals, attorneys

Industry/Entity Type

Real Estate Development

Font styles to use
Sans Serif
Other font styles liked:
• calibri

Colors
0355a3
9bcb3c

Requirements
Must have
• company logo, ability to update text and images
Nice to have
• background image(s) with text overlay
Should not have
• cartoons, harsh colors, stock photos of people, lots of boxes

```html
<!DOCTYPE html>
<html lang="en">
<head>
<meta charset="utf-8">
<title>Stone Valley Engineering PLLC – Land Development Services</title>
<link rel="stylesheet" href="https://fonts.googleapis.com/css2?family=Oswald:wght@300;400&family=Roboto+Condensed:wght@400;700&family=Open+Sans:wght@400;700&family=Source+Sans+3:wght@400;600&display=swap">
<style>
:root{
  --blue:#0355a3;
  --blue-deep:#1d4f97;
  --green:#9bcb3c;
  --green-bright:#8dc63f;
  --charcoal:#3a3a3a;
  --logo-ink:#5b63b7;
  --paper:#eef0f3;
  --white:#ffffff;
  --ink:#1b1b1b;
}
*{margin:0;padding:0;box-sizing:border-box}
html,body{width:848px;height:1200px;overflow:hidden;background:var(--paper)}
.flyer{position:relative;width:848px;height:1200px;background:var(--paper);font-family:"Open Sans",Arial,sans-serif;color:var(--ink)}

.hero{position:absolute;left:0;top:0;width:848px;height:320px;
  background:linear-gradient(180deg,#c9d6d8 0%,#9fb7b8 30%,#6f9193 55%,#4f7466 78%,#3e5f3f 100%)}
.hero-panel{position:absolute;left:0;top:0;width:730px;height:150px;background:rgba(255,255,255,.82);
  clip-path:polygon(0 0,100% 0,88% 100%,0 100%)}
.brand{position:absolute;left:28px;top:24px;display:flex;align-items:center;gap:12px}
.brand-square{width:64px;height:64px;background:var(--logo-ink)}
.brand-name{font-family:"Source Sans 3",Arial,sans-serif;font-size:43px;font-weight:400;color:var(--logo-ink);letter-spacing:-.3px}
.mission{position:absolute;left:100px;top:92px;width:560px;text-align:center;font-family:"Roboto Condensed",Arial,sans-serif;font-size:21px;line-height:26px;color:var(--ink)}

.intro-band{position:absolute;left:0;top:320px;width:848px;height:130px;background:var(--blue-deep);border-top:5px solid var(--green-bright)}
.intro-band p{width:780px;margin:12px auto 0;text-align:center;font-family:"Roboto Condensed",Arial,sans-serif;font-size:17.5px;line-height:23px;color:var(--white)}

.services{position:absolute;left:22px;top:467px;width:806px;display:flex;gap:31px}
.service{width:180px;display:flex;flex-direction:column}
.service-image{height:165px}
.service-title{height:40px;margin:0 -6px;background:var(--blue-deep);color:var(--white);font-family:"Oswald",Arial,sans-serif;font-weight:300;font-size:30px;line-height:40px;text-align:center;letter-spacing:-.3px;white-space:nowrap;border-bottom:3px solid var(--white)}
.service-body{height:312px;margin-top:8px;padding:4px 5px;text-align:center;font-family:"Roboto Condensed",Arial,sans-serif;font-size:13px;line-height:17px}
.service-body strong{display:block;font-weight:700}
.service--dark .service-body{background:var(--charcoal);color:var(--white)}
.service--green .service-body{background:var(--green);color:var(--ink)}
.service--blue .service-body{background:var(--blue-deep);color:var(--white)}

.img-planning{background:linear-gradient(160deg,#f4f4f4,#d9d9d9)}
.img-surveying{background:linear-gradient(180deg,#1f5fae 0%,#4a86c8 60%,#c2452e 100%)}
.img-engineering{background:linear-gradient(180deg,#7fb0d6 0%,#a9c6d6 45%,#8a7a3a 75%,#5a5140 100%)}
.img-environmental{background:linear-gradient(180deg,#dfe9f0 0%,#6f9a4b 40%,#4f7a8a 70%,#5f8a3b 100%)}

.clients-bar{position:absolute;left:44px;top:993px;width:760px;height:30px;background:var(--blue-deep);border:3px solid var(--green-bright);color:var(--white);font-family:"Roboto Condensed",Arial,sans-serif;font-size:14px;line-height:24px;text-align:center;text-transform:uppercase}
.clients{position:absolute;left:30px;top:1035px;width:790px;display:flex;flex-wrap:wrap;justify-content:space-around;row-gap:18px}
.client{width:86px;height:38px;display:flex;align-items:center;justify-content:center;text-align:center;font-family:"Open Sans",Arial,sans-serif;font-weight:700;font-size:12px;line-height:14px;color:var(--blue-deep)}

.footer{position:absolute;left:0;top:1133px;width:848px;height:50px;background:var(--blue-deep);border-top:4px solid #2a67b6;border-bottom:4px solid #2a67b6;display:flex;align-items:center;color:var(--white);font-family:"Open Sans",Arial,sans-serif;font-weight:700;font-size:12.5px}
.contact{display:flex;align-items:center;gap:10px;position:absolute}
.contact svg{width:16px;height:16px}
.contact--address{left:58px}
.contact--phone{left:478px}
.contact--web{left:672px}
</style>
</head>
<body>
<main class="flyer">
  <header class="hero" role="img" aria-label="Misty layered blue-green mountain ridges under a pale sky">
    <div class="hero-panel"></div>
    <div class="brand">
      <span class="brand-square"></span>
      <span class="brand-name">Stone Valley Engineering PLLC</span>
    </div>
    <p class="mission">Our mission at Stone Valley Engineering is to provide Superior Quality Professional Land Development Services</p>
  </header>

  <section class="intro-band">
    <p>Our firm provides planning, surveying, engineering, and environmental services which allows us to focus on the entire land development process rather than one specific discipline. Providing a broad scope of professional services helps to streamline a project by eliminating many disadvantages of having multiple firms with overlapping responsibilities.</p>
  </section>

  <section class="services">
    <article class="service service--dark">
      <div class="service-image img-planning" role="img" aria-label="Site plan drawing of a commercial development with parking and buildings"></div>
      <h2 class="service-title">PLANNING</h2>
      <div class="service-body">
        <strong>We are land development professionals who can see the “big picture”.</strong>
        We have extensive experience with site selection, due diligence investigations, re-zonings, and land planning. Every project is different. We look forward to identifying all feasible alternatives. We become part of the project and enjoy developing the best plan for the success of each particular project. We understand that time is money and unexpected delays are unacceptable
      </div>
    </article>
    <article class="service service--green">
      <div class="service-image img-surveying" role="img" aria-label="GPS survey receiver on a red and yellow tripod against blue sky"></div>
      <h2 class="service-title">SURVEYING</h2>
      <div class="service-body">
        <strong>We are land development professionals who provide superior quality surveying services.</strong>
        Our firm can handle any surveying need. We have extensive experience with ALTA surveys, boundary surveys, subdivision platting, topographic/location surveys, GPS surveys, R/W surveys, construction staking, as-built surveys, elevation certificates, etc. We work closely with title attorneys to provide legal descriptions, exhibits, and other assistance when closing the real estate deal
      </div>
    </article>
    <article class="service service--blue">
      <div class="service-image img-engineering" role="img" aria-label="Excavator with an auger drill on a construction site"></div>
      <h2 class="service-title">ENGINEERING</h2>
      <div class="service-body">
        <strong>We are land development professionals who can handle the most complicated engineering challenge.</strong>
        Let us worry about all the technical stuff and the regulators. Our firm has extensive experience with infrastructure assessments, erosion control, grading, roadway design, stormwater management, water systems, sewer systems, utilities, flood plain management, landscape design, permitting, bidding, and construction administration.
      </div>
    </article>
    <article class="service service--green">
      <div class="service-image img-environmental" role="img" aria-label="Calm river bordered by green trees and tall grass"></div>
      <h2 class="service-title">ENVIRONMENTAL</h2>
      <div class="service-body">
        <strong>We are land development professionals who provide superior quality environmental services.</strong>
        We provide environmental site assessments, underground storage tank management, soil and groundwater sampling and testing, contamination remediation, Brownfields assessments, permitting and redevelopment, and wetlands permitting. Our firm works closely with state and federal agencies to provide economical mitigation and remediation solutions
      </div>
    </article>
  </section>

  <div class="clients-bar">Our business would not be successful without the support of our clients. Some of our project clients include</div>
  <section class="clients">
    <span class="client">Verdo Grill</span>
    <span class="client">Craftway</span>
    <span class="client">Griddle House</span>
    <span class="client">Salsa Joe's</span>
    <span class="client">Crustline</span>
    <span class="client">Burrito Barn</span>
    <span class="client">Gearpoint Auto</span>
    <span class="client">Fieldmark</span>
    <span class="client">Korvana</span>
    <span class="client">Linkwave</span>
    <span class="client">Homeyard</span>
    <span class="client">Farrow Foods</span>
    <span class="client">Taco Lane</span>
    <span class="client">Fresh Cart</span>
    <span class="client">Roastery Co</span>
    <span class="client">Wing Ranch</span>
    <span class="client">Biscuit Barn</span>
    <span class="client">Pawford</span>
  </section>

  <footer class="footer">
    <div class="contact contact--address">
      <svg viewBox="0 0 16 16" fill="none" stroke="#fff" stroke-width="1.5"><path d="M8 15s5-5 5-9a5 5 0 0 0-10 0c0 4 5 9 5 9z"/><circle cx="8" cy="6" r="1.8"/></svg>
      <span>418 Crest Avenue – Suite 300 Millbrook, NC 28731</span>
    </div>
    <div class="contact contact--phone">
      <svg viewBox="0 0 16 16" fill="none" stroke="#fff" stroke-width="1.5"><rect x="4.5" y="1.5" width="7" height="13" rx="1"/></svg>
      <span>(555) 214-7730</span>
    </div>
    <div class="contact contact--web">
      <svg viewBox="0 0 16 16" fill="none" stroke="#fff" stroke-width="1.3"><circle cx="8" cy="8" r="6.5"/><path d="M1.5 8h13M8 1.5c2 2 2 11 0 13M8 1.5c-2 2-2 11 0 13"/></svg>
      <span>www.tovamrk.net</span>
    </div>
  </footer>
</main>
</body>
</html>
```